Kestrelmoor business card

We're looking to "refresh" our original Kestrelmoor logo design and also get a new business card design. We're a modern consulting and software business that's been around 4-years now. We work with large professional companies and therefore require a design that is simple and professional. We would like to retain the notch in the "A" and just the word "Kestrelmoor" as the logo. We like greys, silvers, black, white...but happy to explore highlight color. We're looking for understated modern.

Industry/Entity Type

Software

```html
<!DOCTYPE html>
<html lang="en">
<head>
<meta charset="utf-8">
<title>Kestrelmoor business card</title>
<link rel="stylesheet" href="https://fonts.googleapis.com/css2?family=Barlow:wght@400;500;700;800&display=swap">
<style>
  :root {
    --backdrop: #3b3e3f;
    --brand-yellow: #f2c500;
    --brand-yellow-light: #f7d31a;
    --card-white: #f4f4f3;
    --ink: #3a3a3a;
    --ink-soft: #4a4a4a;
    --shadow: rgba(0, 0, 0, 0.35);
  }
  * { box-sizing: border-box; margin: 0; padding: 0; }
  html, body {
    width: 1200px;
    height: 900px;
    overflow: hidden;
    background: var(--backdrop);
    font-family: "Barlow", Arial, sans-serif;
  }
  .card-sheet {
    position: absolute;
    inset: 0;
    display: flex;
    align-items: center;
    justify-content: center;
    gap: 60px;
  }
  .card {
    position: relative;
    width: 520px;
    height: 318px;
    box-shadow: 0 14px 30px var(--shadow);
    overflow: hidden;
  }
  .card--front {
    background: linear-gradient(135deg, var(--brand-yellow) 0%, var(--brand-yellow-light) 55%, var(--brand-yellow) 100%);
  }
  .card--back {
    background: linear-gradient(135deg, #ffffff 0%, var(--card-white) 60%, #ececeb 100%);
  }
  .wordmark {
    font-weight: 800;
    color: var(--ink);
    letter-spacing: -1px;
    line-height: 1;
  }
  .card--front .wordmark {
    position: absolute;
    right: 36px;
    bottom: 84px;
    font-size: 58px;
  }
  .website {
    position: absolute;
    right: 40px;
    bottom: 56px;
    font-size: 17px;
    font-weight: 500;
    color: var(--ink);
    letter-spacing: 0.3px;
  }
  .card--back .wordmark {
    position: absolute;
    left: 48px;
    top: 44px;
    font-size: 52px;
  }
  .person {
    position: absolute;
    left: 48px;
    top: 132px;
    display: flex;
    gap: 12px;
  }
  .person__marker { margin-top: 5px; }
  .person__name {
    font-size: 20px;
    font-weight: 700;
    color: var(--ink);
  }
  .person__role {
    font-size: 14px;
    font-weight: 500;
    color: var(--ink-soft);
    letter-spacing: 0.5px;
    text-transform: uppercase;
  }
  .contact-list {
    position: absolute;
    left: 48px;
    top: 200px;
    list-style: none;
  }
  .contact-list li {
    display: flex;
    align-items: center;
    gap: 14px;
    font-size: 16px;
    font-weight: 500;
    color: var(--ink);
    height: 26px;
  }
  .contact-list svg { flex: none; }
</style>
</head>
<body>
  <main class="card-sheet">
    <section class="card card--front" aria-label="Business card front">
      <div class="wordmark">Kestrelmoor</div>
      <div class="website">www.kestrelmoor.com.au</div>
    </section>

    <section class="card card--back" aria-label="Business card back">
      <div class="wordmark">Kestrelmoor</div>
      <div class="person">
        <svg class="person__marker" width="12" height="12" viewBox="0 0 12 12" aria-hidden="true">
          <polygon points="1,1 11,6 1,11" fill="var(--brand-yellow)"/>
        </svg>
        <div>
          <div class="person__name">Daniel Hartley</div>
          <div class="person__role">Director</div>
        </div>
      </div>
      <ul class="contact-list">
        <li>
          <svg width="14" height="16" viewBox="0 0 14 16" aria-hidden="true">
            <rect x="3" y="1" width="8" height="14" rx="1.5" fill="none" stroke="var(--brand-yellow)" stroke-width="1.8"/>
            <line x1="5.5" y1="12" x2="8.5" y2="12" stroke="var(--brand-yellow)" stroke-width="1.5"/>
          </svg>
          0412 555 019
        </li>
        <li>
          <svg width="14" height="16" viewBox="0 0 14 16" aria-hidden="true">
            <rect x="1" y="4" width="12" height="9" rx="1" fill="none" stroke="var(--brand-yellow)" stroke-width="1.8"/>
            <polyline points="1.5,4.5 7,9 12.5,4.5" fill="none" stroke="var(--brand-yellow)" stroke-width="1.6"/>
          </svg>
          dhartley@kestrelmoor.com.au
        </li>
        <li>
          <svg width="14" height="16" viewBox="0 0 14 16" aria-hidden="true">
            <path d="M7 1.5a4.5 4.5 0 0 1 4.5 4.5c0 3.2-4.5 8.5-4.5 8.5S2.5 9.2 2.5 6A4.5 4.5 0 0 1 7 1.5z" fill="none" stroke="var(--brand-yellow)" stroke-width="1.8"/>
            <circle cx="7" cy="6" r="1.6" fill="var(--brand-yellow)"/>
          </svg>
          PO Box 456, Strand NSW 1235
        </li>
      </ul>
    </section>
  </main>
</body>
</html>
```